Business Card - Business Consultancy

Newly Established Company, specializing in Business Consultancy, Human Resource Management, Talent Acquisition and Payroll Solutions.

We need a Business card design which portrays "elegance" and a very sleek yet business-like design. We would like a nice blue trimming (which goes well with the logo) to separate the content of the business card at the top. We would also like to see the design using the color silver either as a background or incorporated into it.

The final design should be a Business card which has colors matching the logo; a nice font; the above-mentioned specifics that adheres to the theme of "a stylish and professional business"

FYI: please do not have too fanciful designs.

Industry/Entity Type

Business Consultant

Contact Information for Business Card

Darren Loh
Business Development Director
Opal Staffing Advisory Private Limited
27 Marlow Street, #05-03B
Crescent Harbour Tower
Singapore 061732
Mobile : (+65) 93584617
Email : dloh@opalstaffing-advisory.com
Alternative : opalstaffingadvisory@mailvista.com

Requirements
Must have
• Nice Blue Trimming matching Logo which separates content, see attached
• Design incorporates either a silver background or the use of the color silver
Should not have
• No Fanciful Designs
• No Childish Designs
• No Overly Complicated Designs

```html
<!DOCTYPE html>
<html lang="en">
<head>
<meta charset="UTF-8">
<title>Opal Staffing Advisory – Business Card</title>
<link rel="stylesheet" href="https://fonts.googleapis.com/css2?family=Source+Sans+3:wght@400;600;700&display=swap">
<style>
  :root {
    --stage: #cfd2d6;
    --card: #ffffff;
    --brand-blue: #1a7dc4;
    --silver: #b9bcc1;
    --ink: #1f1f1f;
    --shadow: rgba(0, 0, 0, 0.2);
  }
  * { margin: 0; padding: 0; box-sizing: border-box; }
  html, body {
    width: 1200px;
    height: 844px;
    overflow: hidden;
    background: var(--stage);
    font-family: "Source Sans 3", "Myriad Pro", Arial, sans-serif;
    color: var(--ink);
  }
  .stage { position: relative; width: 1200px; height: 844px; }
  .card {
    position: absolute;
    width: 540px;
    height: 310px;
    background: var(--card);
    box-shadow: 0 10px 26px var(--shadow);
  }
  .card--front { left: 40px; top: 330px; }
  .card--back { left: 620px; top: 190px; }

  .brand {
    position: absolute;
    display: flex;
    align-items: center;
    gap: 12px;
  }
  .brand__dot {
    width: 40px; height: 40px;
    border-radius: 50%;
    background: var(--brand-blue);
    flex: none;
  }
  .brand__name {
    font-weight: 700;
    font-size: 24px;
    color: var(--brand-blue);
    white-space: nowrap;
  }
  .card--front .brand { left: 120px; top: 36px; }

  .trim {
    position: absolute;
    left: 32px; right: 32px; top: 96px;
    height: 3px;
    background: var(--brand-blue);
  }
  .trim::after {
    content: "";
    position: absolute;
    left: 0; right: 0; top: 5px;
    height: 2px;
    background: var(--silver);
  }

  .holder { position: absolute; left: 32px; top: 142px; }
  .holder__name { font-size: 21px; font-weight: 700; color: var(--brand-blue); line-height: 1.1; }
  .holder__title { font-size: 14px; line-height: 1.3; }
  .holder__company { margin-top: 10px; font-size: 15px; font-weight: 600; color: var(--brand-blue); line-height: 1.3; }
  .holder__address { font-size: 15px; line-height: 1.4; margin-top: 4px; }

  .contacts {
    position: absolute;
    right: 24px; top: 114px;
    list-style: none;
    text-align: right;
    font-size: 13px;
    line-height: 1.6;
  }
  .contacts li { display: flex; justify-content: flex-end; align-items: center; gap: 6px; white-space: nowrap; }
  .contacts .icon { width: 11px; height: 11px; fill: var(--brand-blue); flex: none; }

  .card--back .brand { left: 50%; top: 80px; transform: translateX(-50%); }
  .card--back .brand__name { font-size: 28px; }
  .card--back .trim { left: 90px; right: 90px; top: 146px; }
  .tagline {
    position: absolute;
    left: 0; right: 0; top: 170px;
    text-align: center;
    font-size: 17px;
    font-weight: 600;
    color: var(--brand-blue);
  }
</style>
</head>
<body>
<main class="stage">
  <section class="card card--front" aria-label="Business card front">
    <div class="brand">
      <span class="brand__dot"></span>
      <span class="brand__name">Opal Staffing Advisory</span>
    </div>
    <div class="trim"></div>

    <ul class="contacts">
      <li>(+65) 93584617
        <svg class="icon" viewBox="0 0 24 24" aria-hidden="true"><path d="M6.6 10.8a15.1 15.1 0 0 0 6.6 6.6l2.2-2.2a1 1 0 0 1 1-.25 11.4 11.4 0 0 0 3.6.57 1 1 0 0 1 1 1V20a1 1 0 0 1-1 1A17 17 0 0 1 3 4a1 1 0 0 1 1-1h3.5a1 1 0 0 1 1 1c0 1.25.2 2.45.57 3.57a1 1 0 0 1-.25 1z"/></svg>
      </li>
      <li>dloh@opalstaffing-advisory.com
        <svg class="icon" viewBox="0 0 24 24" aria-hidden="true"><path d="M2 5h20v14H2z"/><path d="M2 5l10 8 10-8" fill="none" stroke="#fff" stroke-width="2"/></svg>
      </li>
      <li>opalstaffingadvisory@mailvista.com
        <svg class="icon" viewBox="0 0 24 24" aria-hidden="true"><path d="M2 5h20v14H2z"/><path d="M2 5l10 8 10-8" fill="none" stroke="#fff" stroke-width="2"/></svg>
      </li>
    </ul>

    <div class="holder">
      <p class="holder__name">Darren Loh</p>
      <p class="holder__title">Business Development Director</p>
      <p class="holder__company">Opal Staffing Advisory Private Limited</p>
      <p class="holder__address">27 Marlow Street, #05-03B<br>Crescent Harbour Tower<br>Singapore 061732</p>
    </div>
  </section>

  <section class="card card--back" aria-label="Business card back">
    <div class="brand">
      <span class="brand__dot"></span>
      <span class="brand__name">Opal Staffing Advisory</span>
    </div>
    <div class="trim"></div>
    <p class="tagline">Recruitment | HR Solutions | Business Consultancy</p>
  </section>
</main>
</body>
</html>
```